Minimalist Professional Business Card Design

We will be revamping our marketing materials: Business cards, Website and Catalogs.
Our Overall Design direction is to have a Minimalist artwork with Professionalism and Premium feel. The revamp starts with the new business card design followed by the others. Thus the designer whom work is selected for this job will likely to follow through with the subsequent jobs.

Target Market(s)

Upscale

Industry/Entity Type

Manufacturing

Contact Information for Business Card

For the Business Cards, the following are required:
. Minimalist yet Professional and Premium Feel
. Background Colors: white and / or light pastel yellow and if needed to smoothen the yellow, the light grey can be incorporated. We are changing our corporate bright yellow to either one of the three alternatives:
1. Soylant yellow CMYK (1%, 0%, 52%, 3%)
2. Popcorn yellow CMYK (0%, 0%, 33%, 0%)
3. Papaya yellow CMYK (0%, 0%, 51%, 0%)

Information to be inputed in the business cards:

Name: Barlen Moritova
Position: Managing Director

Company's name: Vellomar Valves Pte. Ltd.
Address: 512 Halvick Lane #07-09B
Singapore 617302
Tel: (65) 6281 4096
Fax: (65) 6294 7118
Email: barlen@vellomarvalves-example.com
Website: www.vellomarvalves-example.com
Skype: Vellomar.Valves
Whatsapp/ Line/ Viber/ WeChat: (65) 9372 6081

Company's Logo
Company's Slogan
Two product photos placed side by side (if this gets into the way of the design, it is OK not to include them)

Font styles to use
Serif

Colors
ffffff

Requirements
Must have
• Minimalist
Should not have
• Messy, crowded, playful

```html
<!DOCTYPE html>
<html lang="en">
<head>
<meta charset="utf-8">
<title>Vellomar Valves – Business Card</title>
<link rel="stylesheet" href="https://fonts.googleapis.com/css2?family=Open+Sans:wght@400;700&family=Playball&display=swap">
<style>
  :root{
    --canvas:#e4e4e4;
    --card-white:#ffffff;
    --card-yellow:#f8f3a8;
    --band-olive:#b3ae6e;
    --ink:#575757;
    --ink-soft:#7a7a7a;
    --rule:#cfcfcf;
    --product-light:#f1ebb0;
    --product-dark:#c9c177;
  }
  *{box-sizing:border-box;margin:0;padding:0}
  html,body{width:1200px;height:1200px;overflow:hidden;background:var(--canvas)}
  body{font-family:"Open Sans",sans-serif;color:var(--ink);position:relative}

  .card{position:absolute;left:180px;width:840px;height:480px;overflow:hidden;
        box-shadow:0 6px 18px rgba(0,0,0,.12)}
  .card__band{position:absolute;left:0;right:0;bottom:0;height:58px;background:var(--band-olive)}

  /* contact side */
  .card--contact{top:70px;background:var(--card-white)}
  .brand{position:absolute;left:50px;top:120px;width:250px;text-align:center}
  .brand__mark{display:block;width:72px;height:72px;margin:0 auto 18px;border-radius:50%;background:var(--ink)}
  .brand__name{font-size:40px;font-weight:700;letter-spacing:2px;color:var(--ink)}
  .divider{position:absolute;left:330px;top:60px;width:1px;height:300px;background:var(--rule)}
  .contact{position:absolute;left:370px;top:62px;right:30px}
  .contact__name{font-size:34px;font-weight:400;letter-spacing:1px;text-transform:uppercase;line-height:1.1}
  .contact__role{font-size:17px;color:var(--ink-soft);margin:4px 0 22px}
  .contact__list{list-style:none;font-size:17px;line-height:1.55}
  .contact__list li{display:flex;align-items:flex-start;gap:10px}
  .contact__list svg{flex:none;width:15px;height:15px;margin-top:6px;fill:var(--ink)}
  .contact__list .gap{margin-top:10px}

  /* brand side */
  .card--brand{top:610px;background:var(--card-yellow)}
  .wordmark{position:absolute;left:60px;top:36px;font-size:82px;font-weight:700;letter-spacing:3px;color:var(--ink)}
  .slogan{position:absolute;left:62px;top:148px;font-family:"Playball",cursive;font-size:26px;color:var(--ink)}
  .social{position:absolute;left:62px;top:200px;font-size:16px;color:var(--ink);line-height:1.9}
  .social__row{display:flex;align-items:center;gap:6px}
  .social__dot{width:14px;height:14px;border-radius:3px;background:var(--ink-soft)}
  .social__text{margin-left:8px}
  .product{position:absolute;right:34px;bottom:72px;width:330px;height:210px;border-radius:6px;
           background:linear-gradient(135deg,var(--product-light),var(--product-dark))}
</style>
</head>
<body>

<section class="card card--contact">
  <div class="brand">
    <span class="brand__mark"></span>
    <div class="brand__name">VELLOMAR</div>
  </div>
  <div class="divider"></div>
  <div class="contact">
    <h1 class="contact__name">Barlen Moritova</h1>
    <p class="contact__role">Managing Director</p>
    <ul class="contact__list">
      <li><svg viewBox="0 0 16 16"><path d="M3 1l3 3-2 2c1 2 4 5 6 6l2-2 3 3-2 2C7 15 1 9 1 3z"/></svg>(65) 6281 4096</li>
      <li><svg viewBox="0 0 16 16"><rect x="4" y="1" width="8" height="5"/><rect x="1" y="6" width="14" height="6"/><rect x="4" y="11" width="8" height="4"/></svg>(65) 6294 7118</li>
      <li class="gap"><svg viewBox="0 0 16 16"><circle cx="8" cy="8" r="7"/></svg>www.vellomarvalves-example.com</li>
      <li><svg viewBox="0 0 16 16"><path d="M1 3h14v10H1z M1 3l7 6 7-6" stroke="#fff" stroke-width="1"/></svg>barlen@vellomarvalves-example.com</li>
      <li class="gap"><svg viewBox="0 0 16 16"><path d="M8 1a5 5 0 0 1 5 5c0 4-5 9-5 9S3 10 3 6a5 5 0 0 1 5-5z"/></svg>512 Halvick Lane #07-09B<br>Singapore 617302</li>
    </ul>
  </div>
  <div class="card__band"></div>
</section>

<section class="card card--brand">
  <div class="wordmark">VELLOMAR</div>
  <p class="slogan">Built With Care &amp; Made To Last</p>
  <div class="social">
    <div class="social__row"><span class="social__dot"></span><span class="social__text">Vellomar.Valves</span></div>
    <div class="social__row"><span class="social__dot"></span><span class="social__dot"></span><span class="social__dot"></span><span class="social__dot"></span><span class="social__text">(65) 9372 6081</span></div>
  </div>
  <div class="product" role="img" aria-label="Two industrial valve products placed side by side, tinted yellow"></div>
  <div class="card__band"></div>
</section>

</body>
</html>
```